Homemaking training schools needs a Business Card design

Designer, Hello!

No special requirements, good-looking enough.
--------------------------------------------------------------------------

Name: Marcus Liao
Chairman
Tel: 0574-57418263
Mobile: 13852247106
Email: kelvory@mailpond.com
Web: www.tqb2031.com
Add: No.258, LinfengJie, DaoyueQu, Ningbo, Zhejiang

LOGO
Ningbo TQB Homemaking Training School

Target Market(s)

pregnant women, mothers, infants, the elderly and families, including cleaning, cooking, nursing training.

Industry/Entity Type

Business

Contact Information for Business Card

Name: Marcus Liao
Chairman
Tel: 0574-57418263
Mobile: 13852247106
Email: kelvory@mailpond.com
Web: www.tqb2031.com

LOGO

Font styles to use
Serif
Sans Serif
Decorative

Requirements
Nice to have
• Feels: clean, specifications, safety, comfort, warmth and happiness.

```html
<!DOCTYPE html>
<html lang="en">
<head>
<meta charset="utf-8">
<title>TianQiBao Business Card</title>
<link rel="stylesheet" href="https://fonts.googleapis.com/css2?family=Open+Sans:wght@400;600;700&display=swap">
<style>
  :root {
    --stage: #3a3532;
    --card-black: #0b0b0b;
    --card-pink: #ec008c;
    --brand-blue: #1f7fc9;
    --accent-pink: #ec008c;
    --text-white: #ffffff;
  }
  * { box-sizing: border-box; margin: 0; padding: 0; }
  html, body {
    width: 1200px; height: 900px; overflow: hidden;
    background: var(--stage);
    font-family: "Open Sans", Arial, sans-serif;
  }
  .stage {
    position: relative; width: 1200px; height: 900px;
    display: flex; align-items: center; justify-content: center; gap: 50px;
  }
  .card {
    position: relative; width: 525px; height: 300px;
    box-shadow: 0 12px 30px rgba(0,0,0,.45);
  }
  .card--front { background: var(--card-black); color: var(--text-white); }
  .card--back { background: var(--card-pink); display: flex; align-items: center; justify-content: center; }

  .brand { display: flex; align-items: center; gap: 10px; }
  .brand__dot { width: 16px; height: 16px; border-radius: 50%; }
  .brand__name { font-weight: 700; letter-spacing: -0.5px; }

  .card--front .brand { position: absolute; top: 66px; left: 0; right: 0; justify-content: center; }
  .card--front .brand__dot { background: var(--accent-pink); }
  .card--front .brand__name { color: var(--brand-blue); font-size: 44px; }

  .card--back .brand__dot { background: var(--text-white); width: 18px; height: 18px; }
  .card--back .brand__name { color: var(--text-white); font-size: 48px; }

  .contacts {
    position: absolute; top: 176px; left: 40px; width: 190px;
    list-style: none; text-align: right; font-size: 15px; line-height: 25px;
  }
  .contacts li { display: flex; justify-content: flex-end; align-items: center; gap: 7px; }
  .contacts svg { width: 12px; height: 12px; flex: none; }

  .person { position: absolute; top: 150px; left: 250px; }
  .person__name { color: var(--accent-pink); font-weight: 700; font-size: 17px; }
  .person__title { font-size: 13px; margin-top: 1px; }
  .person__address { font-size: 14px; line-height: 21px; margin-top: 18px; }
</style>
</head>
<body>
<main class="stage">
  <section class="card card--front">
    <div class="brand">
      <span class="brand__dot"></span>
      <span class="brand__name">TianQiBao</span>
    </div>

    <ul class="contacts">
      <li>0574-57418263
        <svg viewBox="0 0 12 12"><path fill="#ec008c" d="M2 1l2 0 1 3-1.3 1a6 6 0 0 0 3.3 3.3L8 7l3 1v2c0 1-1 1.5-2 1.2A10 10 0 0 1 .8 3C.5 2 1 1 2 1z"/></svg>
      </li>
      <li>13852247106
        <svg viewBox="0 0 12 12"><rect x="3" y="0.5" width="6" height="11" rx="1" fill="none" stroke="#ec008c" stroke-width="1.3"/><circle cx="6" cy="9.5" r=".8" fill="#ec008c"/></svg>
      </li>
      <li>kelvory@mailpond.com
        <svg viewBox="0 0 12 12"><rect x="0.5" y="2" width="11" height="8" rx="1" fill="#ec008c"/><path d="M1 3l5 4 5-4" fill="none" stroke="#0b0b0b" stroke-width="1"/></svg>
      </li>
      <li>www.tqb2031.com
        <svg viewBox="0 0 12 12"><circle cx="6" cy="6" r="5.5" fill="#ec008c"/><path d="M.5 6h11M6 .5c-2.5 3-2.5 8 0 11M6 .5c2.5 3 2.5 8 0 11" fill="none" stroke="#0b0b0b" stroke-width=".8"/></svg>
      </li>
    </ul>

    <div class="person">
      <p class="person__name">Marcus Liao</p>
      <p class="person__title">Chairman</p>
      <p class="person__address">No.258, LinfengJie,<br>DaoyueQu, Ningbo, Zhejiang</p>
    </div>
  </section>

  <section class="card card--back">
    <div class="brand">
      <span class="brand__dot"></span>
      <span class="brand__name">TianQiBao</span>
    </div>
  </section>
</main>
</body>
</html>
```